Web Meeting Company Needs Bullet Point Icons for Power Point Presentation

I need 6 Icons / Buttons built to place into a power point presentation.

I have attached 2 slides. The first slide has the exsisting icons that we are using. On the next slide we need Icons that look similar to those in slide one, but reflect the discriptions that are listed next to the current Icons.

- Crowd Sourcing
- Kick Starters
- Segmentation
- Build A...
- Pop-Ups
- Gamification

On Slide 2 I have also uploaded a screen shot of some icons from GlimmerVault that i think would work from a symbol standpoint

Target Market(s)

Pharma Meeting Planning

Industry/Entity Type

It Company

Requirements
Must have
• Icons
Nice to have
• Icons
Should not have
• Icons

```html
<!DOCTYPE html>
<html lang="en">
<head>
<meta charset="UTF-8">
<title>Audience Engagement Themes</title>
<link href="https://fonts.googleapis.com/css2?family=Arimo:wght@400;700&display=swap" rel="stylesheet">
<style>
  :root {
    --bg: #ffffff;
    --title: #b5398f;
    --label: #f7931e;
    --glyph: #1b1b1b;
    --teal-light: #a6dde6;
    --teal-dark: #2f9bb0;
    --teal-shade: #1d7590;
    --pink-light: #e7aed2;
    --pink-dark: #b9639c;
    --pink-shade: #9a4a80;
    --orange-light: #f8c996;
    --orange-dark: #e39a4c;
    --orange-shade: #b9753a;
  }
  html, body {
    margin: 0;
    padding: 0;
    overflow: hidden;
    background: var(--bg);
  }
  .canvas {
    position: relative;
    width: 1097px;
    height: 1200px;
    background: var(--bg);
    font-family: "Arimo", Arial, sans-serif;
  }
  .title {
    position: absolute;
    top: 152px;
    left: 0;
    width: 1122px;
    margin: 0;
    text-align: center;
    font-weight: 400;
    font-size: 55px;
    color: var(--title);
  }
  .theme-list {
    list-style: none;
    margin: 0;
    padding: 0;
  }
  .theme {
    position: absolute;
    left: 142px;
    display: flex;
    align-items: center;
    height: 112px;
  }
  .theme-icon {
    width: 112px;
    height: 112px;
    flex: none;
  }
  .theme-label {
    margin-left: 34px;
    font-weight: 700;
    font-size: 36px;
    color: var(--label);
  }
  .theme:nth-child(1) { top: 268px; }
  .theme:nth-child(2) { top: 407px; }
  .theme:nth-child(3) { top: 547px; }
  .theme:nth-child(4) { top: 688px; }
  .theme:nth-child(5) { top: 825px; }
  .theme:nth-child(6) { top: 966px; }
  .theme:nth-child(4) .theme-label,
  .theme:nth-child(5) .theme-label { margin-left: 38px; }
  .theme:nth-child(6) .theme-label { margin-left: 30px; }
</style>
</head>
<body>
<main class="canvas">
  <h1 class="title">Audience Engagement Themes</h1>

  <svg width="0" height="0" style="position:absolute">
    <defs>
      <linearGradient id="teal" x1="0" y1="0" x2="1" y2="1">
        <stop offset="0" stop-color="var(--teal-light)"/>
        <stop offset="1" stop-color="var(--teal-dark)"/>
      </linearGradient>
      <linearGradient id="pink" x1="0" y1="0" x2="1" y2="1">
        <stop offset="0" stop-color="var(--pink-light)"/>
        <stop offset="1" stop-color="var(--pink-dark)"/>
      </linearGradient>
      <linearGradient id="orange" x1="0" y1="0" x2="1" y2="1">
        <stop offset="0" stop-color="var(--orange-light)"/>
        <stop offset="1" stop-color="var(--orange-dark)"/>
      </linearGradient>
      <clipPath id="disc"><circle cx="30" cy="30" r="29"/></clipPath>
    </defs>
  </svg>

  <ul class="theme-list">
    <li class="theme">
      <svg class="theme-icon" viewBox="0 0 60 60" aria-hidden="true">
        <circle cx="30" cy="30" r="29" fill="url(#teal)"/>
        <polygon clip-path="url(#disc)" points="42,20 70,48 48,70 20,42" fill="var(--teal-shade)"/>
        <circle cx="30" cy="30" r="15" fill="#fff"/>
        <g fill="var(--teal-shade)">
          <circle cx="30" cy="25" r="3.4"/>
          <path d="M23.5 36 q0-7 6.5-7 q6.5 0 6.5 7z"/>
          <circle cx="22.5" cy="28" r="2.4"/>
          <path d="M18 36 q0-5.5 4.5-5.5 q2 0 3 1 q-2 2-2 4.5z"/>
          <circle cx="37.5" cy="28" r="2.4"/>
          <path d="M42 36 q0-5.5-4.5-5.5 q-2 0-3 1 q2 2 2 4.5z"/>
        </g>
      </svg>
      <span class="theme-label">Crowd Sourcing</span>
    </li>
    <li class="theme">
      <svg class="theme-icon" viewBox="0 0 60 60" aria-hidden="true">
        <circle cx="30" cy="30" r="29" fill="url(#pink)"/>
        <path fill="var(--glyph)" d="M30 12 c2 6 10 11 10 21 a10 10 0 0 1-20 0 c0-5 3-8 5-10 c0 3 1 5 3 6 c-1-6 0-12 2-17z"/>
        <path fill="var(--pink-dark)" d="M30 31 c1 3 4 5 4 8 a4 4 0 0 1-8 0 c0-3 3-5 4-8z"/>
      </svg>
      <span class="theme-label">Kick Starters</span>
    </li>
    <li class="theme">
      <svg class="theme-icon" viewBox="0 0 60 60" aria-hidden="true">
        <circle cx="30" cy="30" r="29" fill="url(#pink)"/>
        <circle cx="30" cy="30" r="14.5" fill="none" stroke="var(--glyph)" stroke-width="5"/>
        <g stroke="var(--pink-light)" stroke-width="2">
          <line x1="30" y1="13" x2="30" y2="19"/>
          <line x1="30" y1="41" x2="30" y2="47"/>
          <line x1="13" y1="30" x2="19" y2="30"/>
          <line x1="41" y1="30" x2="47" y2="30"/>
        </g>
        <circle cx="30" cy="30" r="11" fill="var(--pink-dark)" opacity="0.7"/>
      </svg>
      <span class="theme-label">Segmentation</span>
    </li>
    <li class="theme">
      <svg class="theme-icon" viewBox="0 0 60 60" aria-hidden="true">
        <circle cx="30" cy="30" r="29" fill="url(#teal)"/>
        <g fill="var(--glyph)">
          <path d="M18 16 l7 -2 l6 6 l-3 3 l17 17 l-3 3 l-17-17 l-3 3 l-5-5 l2-2z"/>
          <path d="M44 15 a7 7 0 0 0-9 9 l-18 18 l3 3 l18-18 a7 7 0 0 0 9-9 l-4 4 l-3-1 l-1-3z"/>
        </g>
      </svg>
      <span class="theme-label">Build a…</span>
    </li>
    <li class="theme">
      <svg class="theme-icon" viewBox="0 0 60 60" aria-hidden="true">
        <circle cx="30" cy="30" r="29" fill="url(#orange)"/>
        <polygon clip-path="url(#disc)" points="30,14 44,30 72,58 40,72 16,42" fill="var(--orange-shade)"/>
        <g fill="#fff">
          <rect x="14" y="27" width="6" height="14" rx="1"/>
          <path d="M22 27 l5-4 l2-9 q3 0 3 4 l-1 6 h8 q3 0 2.5 3 q1.5 1 0.5 3 q1.5 1 0 3 q1 2-1.5 3 q0 3-3 3 h-15.5z"/>
        </g>
      </svg>
      <span class="theme-label">Pop Ups</span>
    </li>
    <li class="theme">
      <svg class="theme-icon" viewBox="0 0 60 60" aria-hidden="true">
        <circle cx="30" cy="30" r="29" fill="url(#orange)"/>
        <path fill="var(--glyph)" d="M19 21 h22 q4 0 5 4 l3 12 q1 5-3 5 q-2 0-4-3 l-2-3 h-20 l-2 3 q-2 3-4 3 q-4 0-3-5 l3-12 q1-4 5-4z"/>
        <g fill="var(--orange-light)">
          <rect x="19" y="25" width="2" height="7"/>
          <rect x="16.5" y="27.5" width="7" height="2"/>
          <circle cx="38" cy="26" r="1.2"/>
          <circle cx="40.5" cy="28.5" r="1.2"/>
          <circle cx="35.5" cy="28.5" r="1.2"/>
          <circle cx="38" cy="31" r="1.2"/>
        </g>
      </svg>
      <span class="theme-label">Gamification</span>
    </li>
  </ul>
</main>
</body>
</html>
```